Business Card for: Northbrook Financial Advisory Services Inc.

provide strategic financial advisory services to companies in the areas of corporate finance, mergers and acquisitions, executive coaching and strategic planning

Target Market(s)

Companies, banks, accountants, lawyers

Industry/Entity Type

High end business consulting in corporate finance, mergers and acquisitions, consulting

Contact Information for Business Card

Name of company, Name: xxxxxx xxxxxx , CEO, - phone number: 1-xxx-xxx-xxxx, - email address,

Requirements
Must have
• Must be professional and simple.
Nice to have
• simple, straight graphics, must give the impression that we are trustworthy, professional, competent
Should not have
• loud colors, loud design features

```html
<!DOCTYPE html>
<html lang="en">
<head>
<meta charset="utf-8">
<title>Northbrook Advisory – Business Card</title>
<link href="https://fonts.googleapis.com/css2?family=Inter:wght@300;400;500&display=swap" rel="stylesheet">
<style>
  :root {
    --backdrop: #b5b5b5;
    --card: #1f1f1f;
    --ink: #ffffff;
    --ink-soft: #e6e6e6;
    --rule: #4a4a4a;
  }
  * { box-sizing: border-box; margin: 0; padding: 0; }
  html, body {
    width: 1200px; height: 1200px; overflow: hidden;
    background: var(--backdrop);
    font-family: "Inter", Arial, sans-serif;
  }
  .card {
    position: absolute;
    left: 179px;
    width: 861px;
    height: 496px;
    background: var(--card);
    color: var(--ink);
    box-shadow: 0 10px 24px rgba(0, 0, 0, 0.25);
  }
  .card--front { top: 84px; }
  .card--back { top: 622px; }

  .brand {
    position: absolute;
    left: 0; right: 0;
    text-align: center;
    font-weight: 500;
    font-size: 42px;
    letter-spacing: 0.5px;
    line-height: 1;
    color: var(--ink);
  }
  .card--front .brand { top: 233px; }
  .card--back .brand { top: 127px; }

  .holder {
    position: absolute;
    top: 268px; left: 0; right: 0;
    text-align: center;
    font-size: 28px;
    font-weight: 400;
    line-height: 1;
    letter-spacing: 0.3px;
  }
  .rule {
    position: absolute;
    top: 317px; left: 83px;
    width: 693px; height: 1px;
    background: var(--rule);
  }
  .contact {
    position: absolute;
    top: 333px; left: 0;
    width: 861px; height: 32px;
    font-size: 26px;
    line-height: 1;
    color: var(--ink-soft);
  }
  .contact__label,
  .contact__value { position: absolute; top: 0; white-space: nowrap; }
  .contact__label { font-weight: 400; color: var(--ink); }
  .contact__value { font-weight: 300; }
  .contact__label--phone { left: 84px; }
  .contact__value--phone { left: 137px; }
  .contact__label--email { left: 416px; }
  .contact__value--email { left: 478px; }
  .contact__divider {
    position: absolute;
    left: 367px; top: -3px;
    width: 1.5px; height: 31px;
    background: var(--ink-soft);
  }
</style>
</head>
<body>
  <section class="card card--front">
    <h1 class="brand">Northbrook Advisory</h1>
  </section>

  <section class="card card--back">
    <h2 class="brand">Northbrook Advisory</h2>
    <p class="holder">Daniel Carter - CEO</p>
    <div class="rule"></div>
    <div class="contact">
      <span class="contact__label contact__label--phone">P&nbsp;&nbsp;:</span>
      <span class="contact__value contact__value--phone">1-xxx-xxx-xxxx</span>
      <span class="contact__divider"></span>
      <span class="contact__label contact__label--email">E&nbsp;&nbsp;:</span>
      <span class="contact__value contact__value--email">youremail@yoursite.com</span>
    </div>
  </section>
</body>
</html>
```